Endocrinologist needs new stationery

I have a logo from MarkForge and now need stationery with the new logo.

Address: Suite 4, 282 Falcon Street, Larchmere, ALV 4915
Phone: 03 9417 2253
Fax: 03 9417 2255
Website: www.drmaylacorwen.com.au
Email: admin@drmaylacorwen.com.au

```html
<!DOCTYPE html>
<html lang="en">
<head>
<meta charset="utf-8">
<title>Dr Mayla Corwen Endocrinology – Stationery</title>
<link href="https://fonts.googleapis.com/css2?family=EB+Garamond:wght@400&display=swap" rel="stylesheet">
<style>
  :root {
    --backdrop: #e8e7e3;
    --paper: #fbfbfa;
    --brand-blue: #3d6e9e;
    --ink-grey: #5a5a5a;
    --rule-grey: #9a9a9a;
    --shadow: rgba(0, 0, 0, 0.10);
  }
  html, body {
    margin: 0;
    padding: 0;
    overflow: hidden;
  }
  body {
    width: 795px;
    height: 1200px;
    background: var(--backdrop);
    position: relative;
    font-family: "EB Garamond", Georgia, serif;
  }
  .sheet {
    position: absolute;
    background: var(--paper);
    box-shadow: 0 2px 10px var(--shadow);
  }
  .letterhead {
    left: 157px;
    top: 50px;
    width: 480px;
    height: 679px;
  }
  .card {
    width: 340px;
    height: 194px;
    top: 800px;
  }
  .card-back { left: 40px; }
  .card-front { left: 415px; }

  .wordmark {
    color: var(--brand-blue);
    font-weight: 400;
    white-space: nowrap;
    letter-spacing: 0.02em;
  }
  .rule {
    height: 1px;
    background: var(--rule-grey);
  }

  /* letterhead header: rule, wordmark, rule */
  .letterhead-header {
    position: absolute;
    left: 0;
    right: 0;
    top: 28px;
    display: flex;
    align-items: center;
    gap: 10px;
  }
  .letterhead-header .rule-left { width: 34px; flex: none; }
  .letterhead-header .wordmark { font-size: 19px; flex: none; }
  .letterhead-header .rule-right { flex: 1; }

  .contact {
    position: absolute;
    margin: 0;
    color: var(--ink-grey);
    line-height: 1.3;
    white-space: nowrap;
  }
  .contact .label { color: var(--brand-blue); }
  .letterhead .contact { left: 275px; bottom: 40px; font-size: 12.5px; }

  /* business card back */
  .card-back .contact { left: 26px; top: 22px; font-size: 12px; }
  .card-back .wordmark { position: absolute; right: 26px; bottom: 34px; font-size: 16px; }
  .card-back .rule-under { position: absolute; left: 0; right: 26px; bottom: 26px; }

  /* business card front */
  .card-front .wordmark { position: absolute; left: 50%; top: 82px; transform: translateX(-50%); font-size: 20px; }
  .card-front .rule-short { position: absolute; right: 40px; width: 60px; top: 116px; }
</style>
</head>
<body>
  <section class="sheet letterhead" aria-label="Letterhead">
    <div class="letterhead-header">
      <div class="rule rule-left"></div>
      <div class="wordmark">Dr Mayla Corwen Endocrinology</div>
      <div class="rule rule-right"></div>
    </div>
    <p class="contact">
      <span class="label">Fax:</span> 03 9417 2255<br>
      <span class="label">Phone:</span> 03 9417 2253<br>
      <span class="label">Website:</span> www.drmaylacorwen.com.au<br>
      <span class="label">Email:</span> admin@drmaylacorwen.com.au<br>
      <span class="label">Address:</span> Suite 4, 282 Falcon Street,<br>
      Larchmere, ALV 4915
    </p>
  </section>

  <section class="sheet card card-back" aria-label="Business card, back">
    <p class="contact">
      <span class="label">Fax:</span> 03 9417 2255<br>
      <span class="label">Phone:</span> 03 9417 2253<br>
      <span class="label">Website:</span> www.drmaylacorwen.com.au<br>
      <span class="label">Email:</span> admin@drmaylacorwen.com.au<br>
      <span class="label">Address:</span> Suite 4, 282 Falcon Street,<br>
      Larchmere, ALV 4915
    </p>
    <div class="wordmark">Dr Mayla Corwen Endocrinology</div>
    <div class="rule rule-under"></div>
  </section>

  <section class="sheet card card-front" aria-label="Business card, front">
    <div class="wordmark">Dr Mayla Corwen Endocrinology</div>
    <div class="rule rule-short"></div>
  </section>
</body>
</html>
```